Vertice Norte needs the best stationery in the development business

We need a stationary design for a new company based in Porto, Portugal. We are a new property development management company specialized in downtown regeneration projects and adaptive use of old big textile factories.

We just have selected our new logo in a pixelhive competition and now we are searching for the best stationary design. We expect to receive proposals for:

Two sided business cards
A4 main letterhead
A4 simple text papper
A4 and A5 envelops
A4 single folder front page

information for the stationary project

company signature: RaizProjetoFuturo (as in the logo files attached)

Business card information: 
Henrique Moura Salgado MBQS
Managing Director

email: henrique@verticenorte.example.pt
website: www.verticenorte.example.pt

adress: 
R. das Oliveiras, 71 - 2º
4100-218 Porto

office number
+(351) 22 418 76 03
fax number
+(351) 22 418 76 05
mobile
+(351) 913 204 671

Target Market(s)

professional finantial fund managers and big property owners

Industry/Entity Type

Business

Requirements
Must have
• the company logo

Nice to have
• clear simple contemporary design is appreciated

```html
<!DOCTYPE html>
<html lang="pt">
<head>
<meta charset="utf-8">
<title>Vertice Norte — Envelope</title>
<link rel="stylesheet" href="https://fonts.googleapis.com/css2?family=Archivo:wght@400;600&family=Tinos&display=swap">
<style>
  :root {
    --backdrop: #a9a9a9;
    --paper: #ffffff;
    --brand-blue: #2f56a6;
    --ink: #333333;
    --link-blue: #4a6fc0;
  }
  html, body {
    margin: 0;
    width: 1200px;
    height: 900px;
    overflow: hidden;
    background: var(--backdrop);
  }
  .envelope {
    position: absolute;
    left: 110px;
    top: 135px;
    width: 980px;
    height: 630px;
    background: var(--paper);
    box-shadow: 0 6px 18px rgba(0,0,0,0.25);
  }
  .sender {
    position: absolute;
    left: 0;
    top: 250px;
    width: 420px;
  }
  .brand {
    display: flex;
    align-items: center;
    gap: 12px;
    margin-left: 70px;
  }
  .brand-dot {
    width: 26px;
    height: 26px;
    border-radius: 50%;
    background: var(--brand-blue);
  }
  .brand-name {
    font-family: "Archivo", sans-serif;
    font-weight: 600;
    font-size: 34px;
    letter-spacing: -0.5px;
    color: var(--brand-blue);
    line-height: 1;
  }
  .signature {
    margin: 6px 0 0 108px;
    font-family: "Archivo", sans-serif;
    font-size: 13px;
    color: var(--brand-blue);
  }
  .rule {
    height: 2px;
    background: var(--brand-blue);
    margin-top: 6px;
    width: 420px;
  }
  .contact {
    list-style: none;
    margin: 14px 0 0 70px;
    padding: 0;
    font-family: "Tinos", serif;
    font-size: 14px;
    color: var(--ink);
  }
  .contact li {
    display: flex;
    align-items: flex-start;
    gap: 10px;
    margin-bottom: 8px;
    line-height: 1.3;
  }
  .contact svg {
    flex: none;
    margin-top: 2px;
  }
  .contact .web {
    color: var(--link-blue);
  }
</style>
</head>
<body>
  <main class="envelope">
    <section class="sender">
      <div class="brand">
        <span class="brand-dot"></span>
        <span class="brand-name">Vertice Norte</span>
      </div>
      <p class="signature">RaizProjetoFuturo</p>
      <div class="rule"></div>
      <ul class="contact">
        <li>
          <svg width="12" height="12" viewBox="0 0 12 12" aria-hidden="true">
            <circle cx="6" cy="6" r="6" fill="var(--brand-blue)"/>
            <path d="M6 2.6a2 2 0 0 0-2 2c0 1.5 2 4 2 4s2-2.5 2-4a2 2 0 0 0-2-2z" fill="#fff"/>
          </svg>
          <span>R. das Oliveiras, 71 - 2º<br>4100-218 Porto</span>
        </li>
        <li>
          <svg width="12" height="12" viewBox="0 0 12 12" aria-hidden="true">
            <circle cx="6" cy="6" r="6" fill="var(--brand-blue)"/>
            <circle cx="6" cy="6" r="3.2" fill="none" stroke="#fff" stroke-width="0.8"/>
            <path d="M2.8 6h6.4M6 2.8v6.4" stroke="#fff" stroke-width="0.8"/>
          </svg>
          <span class="web">www.verticenorte.example.pt</span>
        </li>
      </ul>
    </section>
  </main>
</body>
</html>
```